Skincare,Bodycare and haircare brochure

Please design a A4 3 fold brochure for Vexmira Pty Ltd. You may go to our website www.vexmira.example to understand what we do - certified organic skincare.
Content:

About Us: Our Mission
Vexmira’s mission is to make premium skin care products using only certified organic ingredients for a safer, purer world.

How are we diferent?
Vexmira specialises in the research and development of certified organic skin, hair and personal care products for everyone. We hold Certified Organic Licenses with the Verdant Tally Board who accredits our system with the Federal Harvest Purity Code of Australia and other international organic certification standards. Vexmira’s passion is to produce and deliver premium, safe and effective certified organic products to all of our customers.

Other headings: Skincare, Body Care, Hair Care, Essential Oils (leave room for us to put product pictures and product info (you can copy 3 products from each category from our website for draft),

Please provide a heading about our memberships: Please also see our website for info.

Then have a contact us section (doesn't have to be a page) It can even be on the front page.

Please also use the Attached logos. Please use vexmira logo with underline (company logo) and dunbrook crafted and Certified Organic logos.

Many deaigns dont allow me to put alotnof product infronation on it. please allow me to donsoMan

```html
<!DOCTYPE html>
<html lang="en">
<head>
<meta charset="utf-8">
<title>Vexmira – Our Products Brochure</title>
<link href="https://fonts.googleapis.com/css2?family=Inter:wght@300;400&family=Roboto:wght@300&family=Roboto+Condensed:wght@700&display=swap" rel="stylesheet">
<style>
  :root {
    --page: #ffffff;
    --sand: #dcc2a1;
    --ink: #111111;
    --black: #000000;
    --white: #ffffff;
    --shot-dark: #3a2418;
    --shot-amber: #8a4a20;
    --shot-pale: #cfd6c4;
  }
  * { margin: 0; padding: 0; box-sizing: border-box; }
  html, body { width: 1200px; height: 938px; overflow: hidden; background: var(--page); }
  .brochure {
    position: absolute; left: 67px; top: 57px; width: 1066px; height: 823px;
    background: var(--sand);
    box-shadow: 4px 5px 6px rgba(0,0,0,.45);
    font-family: "Inter", Helvetica, Arial, sans-serif;
    color: var(--ink);
  }
  .about-panel { position: absolute; left: 0; top: 0; width: 356px; height: 823px; background: var(--black); color: var(--white); }
  .hero-photo {
    position: absolute; left: 0; top: 0; width: 356px; height: 293px;
    background: linear-gradient(90deg, #d8c296 0%, #e3cfa6 25%, #f1e6de 45%, #e9c7b0 60%, #d9c08f 85%, #cdb27f 100%);
  }
  .about-heading { position: absolute; left: 66px; font-weight: 300; font-size: 22px; line-height: 26px; }
  .about-text {
    position: absolute; left: 66px; width: 226px;
    font-family: "Roboto", Helvetica, Arial, sans-serif; font-weight: 300;
    font-size: 11.3px; line-height: 21.6px; text-align: justify;
  }
  .products-bar {
    position: absolute; left: 356px; top: 33px; width: 710px; height: 23px; background: var(--black);
    color: var(--white); font-size: 15px; line-height: 23px; letter-spacing: 37.5px; padding-left: 90px; white-space: pre; overflow: hidden;
  }
  .category-title { position: absolute; font-weight: 400; font-size: 45px; line-height: 40px; letter-spacing: -1px; }
  .category-sub { position: absolute; font-weight: 300; font-size: 16px; letter-spacing: 3.4px; line-height: 18px; }
  .category-lead {
    position: absolute; font-family: "Roboto Condensed", Arial, sans-serif; font-weight: 700;
    font-size: 12.5px; line-height: 16px;
  }
  .product-list {
    position: absolute; list-style: none;
    font-family: "Roboto Condensed", Arial, sans-serif; font-weight: 700; font-size: 10px;
  }
  .product-list li::before { content: "•"; margin-right: 4px; }
  .skin-list li { line-height: 17.6px; }
  .body-list li { line-height: 18.8px; }
  .hair-list li { line-height: 19px; }
  .oil-list li { line-height: 16.2px; }
  .product-shot { position: absolute; border-radius: 6px; }
  .skin-shot { left: 378px; top: 228px; width: 110px; height: 120px;
    background: linear-gradient(160deg, var(--shot-pale), var(--shot-dark)); }
  .hair-shot { left: 755px; top: 151px; width: 74px; height: 210px;
    background: linear-gradient(180deg, var(--shot-dark), var(--shot-amber)); }
  .body-shot { left: 566px; top: 453px; width: 82px; height: 328px;
    background: linear-gradient(180deg, var(--shot-dark), var(--shot-pale) 40%, var(--shot-pale)); }
  .oil-shot { left: 945px; top: 378px; width: 86px; height: 215px;
    background: linear-gradient(180deg, var(--shot-dark), var(--shot-pale) 45%, var(--shot-pale)); }
</style>
</head>
<body>
<main class="brochure">
  <section class="about-panel">
    <div class="hero-photo" role="img" aria-label="Spa photo: woman with a white towel wrapped on her head receiving a facial massage on a bamboo mat"></div>
    <h2 class="about-heading" style="top:350px">Our Mission</h2>
    <p class="about-text" style="top:378px">Vexmira’s mission is to make premium skin care products using only certified organic ingredients for a safer, purer world.</p>
    <h2 class="about-heading" style="top:479px">How are we diferent?</h2>
    <p class="about-text" style="top:507px">Vexmira specialises in the research and development of certified organic skin, hair and personal care products for everyone. We hold Certified Organic Licenses with the Verdant Tally Board who accredits our system with the Federal Harvest Purity Code of Australia and other international organic certification standards. Vexmira’s passion is to produce and deliver premium, safe and effective certified organic products to all of our customers.</p>
  </section>

  <div class="products-bar">OUR PRODUCTS</div>

  <h2 class="category-title" style="left:437px;top:106px">Skincare</h2>
  <p class="category-sub" style="left:515px;top:145px">Products</p>
  <p class="category-lead" style="left:503px;top:173px">Organic Products for your Skin</p>
  <ul class="product-list skin-list" style="left:516px;top:192px">
    <li>Moisturising Cream</li><li>Eye Cream</li><li>Lip Balm</li><li>Aloe Vera Gel</li>
    <li>Australian Native Facial Cleansing Gel</li><li>Makeup Remover - Blueberry Extract</li>
    <li>Certified Organic Lip Blam - Mint</li><li>Face Pearl Exfoliant - Super Fine</li>
    <li>Rosa Cranina Face Exfoliant</li><li>Skin Brightening Serum</li>
    <li>Australian Antioxidant Primer</li><li>Antioxidant Boost Facial Mask</li>
  </ul>
  <div class="product-shot skin-shot" role="img" aria-label="Product photo: jar of organic skin cream"></div>

  <h2 class="category-title" style="left:789px;top:107px">Shampoo</h2>
  <p class="category-lead" style="left:853px;top:164px">Certified Organic Products<br>for your Body</p>
  <ul class="product-list hair-list" style="left:853px;top:208px">
    <li>Shampoo</li><li>Conditioner</li>
  </ul>
  <div class="product-shot hair-shot" role="img" aria-label="Product photo: pump bottle of organic shampoo"></div>

  <h2 class="category-title" style="left:750px;top:378px;font-size:45px;line-height:42px">Essential<br>Oils</h2>
  <p class="category-lead" style="left:750px;top:465px">Certified Organic Oils</p>
  <ul class="product-list oil-list" style="left:750px;top:494px">
    <li>Clementine</li><li>Lavadin Grosso</li><li>Lemongrass</li><li>Peppermint Premium</li><li>Ylang Yalng</li>
    <li>Certified Organic Ginger Essential Oil</li><li>Certified Organic Lavender Essential Oil</li>
    <li>Certified Organic Lemon Essential Oil</li><li>Certified Organic Mandarin Essential Oil</li>
    <li>Certified Organic Rosemary Essential Oil</li><li>Certified Organic Sandalwood Australian</li>
    <li>Certified Organic Tea Tree Essential Oil</li><li>Certified Organic Tea Tree Lemon Scented Oil</li>
    <li>Certified Organic Chamomile German Blue</li><li>Certified Organic Eucalyptus Essential Oil</li>
    <li>Certified Organic Lavadin Grosso Essential Oil</li><li>Lime</li>
  </ul>
  <div class="product-shot oil-shot" role="img" aria-label="Product photo: small dropper bottle of essential oil"></div>

  <h2 class="category-title" style="left:410px;top:487px">Body<br>Care</h2>
  <p class="category-sub" style="left:410px;top:566px">Products</p>
  <p class="category-lead" style="left:410px;top:601px">Certified Organic products<br>for your Body</p>
  <ul class="product-list body-list" style="left:410px;top:638px">
    <li>Shower and Bath Gel</li><li>Body Lotion</li><li>Body Custard</li><li>Hand Cream</li><li>Sugar Scrub</li>
  </ul>
  <div class="product-shot body-shot" role="img" aria-label="Product photo: pump bottle of certified organic body lotion"></div>
</main>
</body>
</html>
```